Australian Civil Construction, Quarry & Mining Services needs a business card

We need a business card designed for our Civil Construction, Quarry & Mining Services based in the country in Australia.
Our Company Brackley Earthworks provide innovate solutions for infrastructure, agricultural and mining (aggregate, sand, roadbase) industry.
We would like our business cards to be double sided
Front of card: black background or something that resembles our business colours. (it doesn't have to be black we are open to options)
- Company name - Brackley Earthworks
- Either our logo or some sort of icon/picture that resembles our business
- Website - https://brackleyearthworks.com.au/
- We will have a number of different names, positions descriptions, phone numbers and emails on separate cards for each of our managers/directors

```html
<!DOCTYPE html>
<html lang="en">
<head>
<meta charset="utf-8">
<title>Brackley Earthworks – Business Card</title>
<link rel="stylesheet" href="https://fonts.googleapis.com/css2?family=Archivo+Black&family=Barlow+Condensed:ital,wght@0,500;0,600;1,600&display=swap">
<style>
  :root {
    --canvas: #c8c8c8;
    --card: #000000;
    --disc: #161213;
    --orange: #f07a14;
    --orange-deep: #b3530f;
    --rust: #a84d0c;
    --white: #ffffff;
  }
  html, body {
    margin: 0;
    width: 1200px;
    height: 1200px;
    overflow: hidden;
    background: var(--canvas);
  }
  .card {
    position: absolute;
    left: 221px;
    width: 758px;
    height: 438px;
    display: block;
    background: var(--card);
  }
  .card--front { top: 142px; }
  .card--back  { top: 619px; }

  .wordmark {
    font-family: "Archivo Black", "Arial Black", sans-serif;
    fill: var(--rust);
  }
  .brand-name {
    font-family: "Archivo Black", "Arial Black", sans-serif;
    fill: var(--white);
  }
  .person-first { font-family: "Barlow Condensed", sans-serif; font-weight: 600; fill: var(--white); }
  .person-last  { fill: var(--orange); }
  .person-role  { font-family: "Barlow Condensed", sans-serif; font-weight: 600; font-style: italic; fill: var(--white); }
  .contact-line { font-family: "Barlow Condensed", sans-serif; font-weight: 500; fill: var(--white); }
  .icon { fill: var(--white); }
  .icon-stroke { fill: none; stroke: var(--white); stroke-width: 1.7; }
</style>
</head>
<body>

<!-- Front of card -->
<svg class="card card--front" viewBox="0 0 758 438" aria-label="Card front">
  <rect width="758" height="438" fill="var(--card)"/>

  <g class="feature-name">
    <text class="brand-name" x="10" y="150" font-size="60" textLength="250" lengthAdjust="spacingAndGlyphs">BRACKLEY</text>
    <text class="brand-name" x="10" y="240" font-size="60" textLength="250" lengthAdjust="spacingAndGlyphs">EARTH</text>
    <text class="brand-name" x="10" y="330" font-size="60" textLength="250" lengthAdjust="spacingAndGlyphs">WORKS</text>
  </g>

  <circle class="brand-disc" cx="505" cy="145" r="119" fill="var(--disc)"/>
  <text class="brand-name" x="505" y="141" font-size="24" text-anchor="middle" textLength="140" lengthAdjust="spacingAndGlyphs">BRACKLEY</text>
  <text class="brand-name" x="505" y="171" font-size="24" text-anchor="middle" textLength="170" lengthAdjust="spacingAndGlyphs">EARTHWORKS</text>

  <text class="wordmark" x="505" y="322" font-size="60" text-anchor="middle" textLength="292" lengthAdjust="spacingAndGlyphs">BRACKLEY</text>
  <text class="wordmark" x="505" y="387" font-size="60" text-anchor="middle" textLength="413" lengthAdjust="spacingAndGlyphs">EARTHWORKS</text>
</svg>

<!-- Back of card -->
<svg class="card card--back" viewBox="0 0 758 438" aria-label="Card back">
  <defs>
    <linearGradient id="bandGradient" x1="0" y1="0" x2="1" y2="0">
      <stop offset="0" stop-color="var(--orange)"/>
      <stop offset="1" stop-color="var(--orange-deep)"/>
    </linearGradient>
  </defs>
  <rect width="758" height="438" fill="var(--card)"/>
  <polygon class="accent-band" points="0,0 107,0 360,438 192,438 0,104" fill="url(#bandGradient)"/>
  <circle class="brand-disc" cx="188" cy="219" r="159" fill="var(--disc)"/>
  <text class="brand-name" x="188" y="214" font-size="30" text-anchor="middle" textLength="170" lengthAdjust="spacingAndGlyphs">BRACKLEY</text>
  <text class="brand-name" x="188" y="250" font-size="30" text-anchor="middle" textLength="210" lengthAdjust="spacingAndGlyphs">EARTHWORKS</text>

  <text class="person-first" x="714" y="108" font-size="45" text-anchor="end">FIRST <tspan class="person-last">LASTNAME</tspan></text>
  <text class="person-role" x="709" y="140" font-size="29" text-anchor="end">Manager</text>

  <!-- phone -->
  <path class="icon" d="M366 228 q-3 0 -4 4 q-1 9 7 18 q8 9 14 9 q3 0 4 -3 l-1 -4 l-6 -2 l-2 2 q-6 -3 -9 -11 l2 -2 l-1 -6 z"/>
  <text class="contact-line" x="398" y="245" font-size="29.5">01 2345 6789</text>

  <!-- email -->
  <rect class="icon" x="358" y="270" width="28" height="20" rx="3"/>
  <path d="M363 276 l9 6.5 l9 -6.5" fill="none" stroke="var(--card)" stroke-width="2.2" stroke-linecap="round"/>
  <text class="contact-line" x="398" y="289" font-size="29.5">name@emailname.com.au</text>

  <!-- web -->
  <circle class="icon-stroke" cx="372" cy="323" r="11"/>
  <ellipse class="icon-stroke" cx="372" cy="323" rx="4.8" ry="11"/>
  <line class="icon-stroke" x1="361" y1="323" x2="383" y2="323"/>
  <line class="icon-stroke" x1="362.5" y1="317" x2="381.5" y2="317"/>
  <line class="icon-stroke" x1="362.5" y1="329" x2="381.5" y2="329"/>
  <text class="contact-line" x="398" y="332" font-size="29.5">websitename.com.au</text>
</svg>

</body>
</html>
```